innovative investment real estate sales firm

We are a uniquely collabrative firm that seeks to bring a conultative approach to uncovering hidden opportunities for our clients, our website needs to convey our client focused approach. Our firm specializes in the sale of apartment properties in Southern California. We have a team of researchers, transaction coordinators and marketing personal to support our geographically specialized advisers. We need a website that introduces clients to our unique way of better helping them achieve their investment goals.

Target Market(s)

High net worth individuals and families

Industry/Entity Type

Real Estate Agent

Font styles to use
Other font styles liked:
• please use font provided

Requirements
Must have
• Stories of our recent projects
• Features on our people
• email capture for viewing inventory
• content that showcases our unique consultative approach that uncovers unrealized opportunities

```html
<!DOCTYPE html>
<html lang="en">
<head>
<meta charset="utf-8">
<title>Meridian Advisers – Real Estate Investing</title>
<link href="https://fonts.googleapis.com/css2?family=Poppins:wght@400;500;600&family=Open+Sans:wght@400;600;700&display=swap" rel="stylesheet">
<style>
:root{
  --green:#8cc63f;
  --teal:#1b9bb3;
  --ink:#222;
  --text:#666;
  --muted:#999;
  --line:#e3e3e3;
  --grey-bg:#f1f2f3;
  --panel-green:#1e3a28;
  --panel-teal:#0e4a52;
  --footer:#2a2a2a;
  --footer-bottom:#222;
  --white:#fff;
}
*{box-sizing:border-box;margin:0;padding:0}
html,body{width:1200px;height:3255px;overflow:hidden}
body{font-family:"Open Sans",Arial,sans-serif;color:var(--text);background:var(--white);font-size:14px;line-height:1.6}
h1,h2,h3,h4,.heading{font-family:"Poppins",Arial,sans-serif;color:var(--ink);font-weight:500}
.wrap{width:980px;margin:0 auto;position:relative}
a{color:inherit;text-decoration:none}
.btn{display:inline-block;font-family:"Poppins",Arial,sans-serif;font-size:13px;font-weight:500;padding:10px 24px;border-radius:2px}
.btn-green{background:var(--green);color:var(--white)}
.btn-outline{border:1px solid var(--white);color:var(--white)}

/* header */
.site-header{height:82px;display:flex;align-items:center}
.site-header .wrap{display:flex;align-items:center;justify-content:space-between}
.brand{display:flex;align-items:center;gap:10px;font-family:"Poppins",Arial,sans-serif;font-weight:600;font-size:18px;color:var(--panel-teal);letter-spacing:1px;text-transform:uppercase}
.brand-mark{width:34px;height:34px;background:var(--teal)}
.main-nav{display:flex;align-items:center;gap:30px;font-size:13px;color:#444}
.main-nav .btn{padding:7px 16px;font-size:12px}
.btn-login{border:1px solid #999;color:#333}

/* hero */
.hero{height:515px;position:relative;background:linear-gradient(100deg,#e7ecef 0%,#c9d4da 45%,#a8b5bb 100%)}
.hero-photo{position:absolute;inset:0}
.hero-copy{position:absolute;left:110px;top:125px;width:520px}
.hero-copy h1{font-size:35px;line-height:1.15;font-weight:600;margin-bottom:18px}
.hero-copy p{font-size:14px;color:#333;line-height:1.45;margin-bottom:26px}
.hero-copy .btn{padding:12px 26px}
.hero-dots{position:absolute;right:110px;top:455px;display:flex;gap:5px}
.hero-dots span{width:12px;height:12px;border-radius:50%;border:1px solid var(--white)}
.hero-dots span:first-child{background:var(--teal);border-color:var(--teal)}
.stats{position:absolute;left:110px;bottom:30px;width:980px;display:flex;background:rgba(255,255,255,.92)}
.stat{flex:1;text-align:center;padding:14px 0 12px;border-right:1px solid var(--line)}
.stat:last-child{border-right:0}
.stat strong{display:block;font-size:13px;color:var(--ink);font-weight:600}
.stat small{font-size:10px;color:var(--muted)}

/* testimonial */
.testimonial{height:113px;border-bottom:1px solid var(--line);display:flex;align-items:center}
.testimonial .wrap{display:flex;align-items:center;justify-content:center;gap:24px}
.arrow{width:20px;height:20px}
.avatar{width:50px;height:50px;border-radius:50%;background:radial-gradient(circle,#e9c6a8,#b98b6b);position:relative}
.avatar::after{content:"";position:absolute;top:-4px;left:-4px;width:18px;height:18px;border-radius:50%;background:var(--teal)}
.quote{text-align:center;font-style:italic;font-size:13px;color:#777;width:560px;line-height:1.5}
.quote cite{display:block;color:var(--teal);font-weight:700;font-size:12px}

/* intro */
.intro{height:480px;background:var(--grey-bg);position:relative;overflow:hidden}
.intro-copy{position:absolute;left:110px;top:60px;width:400px}
.intro-copy h2{font-size:23px;line-height:1.3;margin-bottom:18px}
.intro-copy p{font-size:12.5px;color:#888;line-height:1.75;margin-bottom:20px}
.checks li{list-style:none;display:flex;align-items:center;gap:10px;font-size:15px;color:#555;margin-bottom:8px}
.checks b{color:#333;font-weight:600}
.checks .hl{color:var(--teal);font-weight:600}
.intro-device{position:absolute;left:580px;top:20px;width:540px;height:440px;background:linear-gradient(135deg,#f7f7f7,#d9dcdf);border-radius:6px}

/* how it works */
.how{height:520px;position:relative}
.how-photo{position:absolute;left:110px;top:70px;width:520px;height:340px;background:linear-gradient(120deg,#eef1f3,#bcc7cc)}
.how-copy{position:absolute;left:697px;top:70px;width:390px}
.how-copy h2{font-size:21px;margin-bottom:18px}
.step h3{font-size:16px;color:var(--teal);margin-bottom:6px}
.step p{font-size:12.5px;color:#777;line-height:1.7;margin-bottom:14px}

/* split panels */
.split{height:417px;display:flex}
.panel{flex:1;padding:60px 0 0 110px;color:#d5dcd8;position:relative}
.panel-green{background:linear-gradient(180deg,#284a35,var(--panel-green))}
.panel-teal{background:linear-gradient(180deg,#125b64,var(--panel-teal));padding-left:30px}
.panel h2{color:var(--white);font-size:22px;line-height:1.3;margin-bottom:18px;font-weight:500}
.panel p{font-size:12.5px;line-height:1.75;width:460px;margin-bottom:36px}
.panel .btn{padding:9px 20px}

/* investments */
.investments{height:571px;padding-top:60px}
.investments-head{display:flex;justify-content:space-between;align-items:center;margin-bottom:22px}
.investments-head h2{font-size:21px}
.slider-ctrl{display:flex;gap:4px}
.slider-ctrl span{width:18px;height:18px;border-radius:50%;border:1px solid #ccc}
.slider-ctrl span:last-child{border-color:var(--teal)}
.cards{display:flex;gap:17px}
.card{width:232px;border:1px solid var(--line);text-align:center;padding-bottom:14px}
.card-photo{height:208px}
.card h3{font-size:15px;color:var(--teal);margin:20px 0 14px;font-weight:500}
.card p{font-size:11px;color:#777;margin-bottom:10px}
.card p b{color:#333}

/* cta */
.cta{height:282px;background:linear-gradient(180deg,#dce8ea,#b9d2d6);text-align:center;padding-top:62px}
.cta h2{font-size:22px;margin-bottom:14px}
.cta p{width:780px;margin:0 auto 30px;font-size:13px;color:#7b8c90;line-height:1.7}
.cta .btn{padding:11px 24px}

/* footer */
.site-footer{height:232px;background:var(--footer);color:#aaa;padding-top:32px;font-size:11px}
.footer-cols{display:flex}
.footer-col h4{color:var(--white);font-size:13px;margin-bottom:12px}
.col-join{width:320px}
.col-sub{width:250px}
.col-links{width:185px}
.col-blog{width:225px}
.footer-col p,.footer-col li{line-height:1.6;list-style:none}
.email-field{display:block;width:218px;height:34px;background:var(--white);border-radius:2px;margin:14px 0 10px;padding:8px 12px;color:#aaa}
.subscribe{display:block;width:218px;height:34px;background:var(--green);color:var(--white);text-align:center;line-height:34px;font-weight:600;font-size:12px}
.post{margin-bottom:12px}
.post .meta{font-size:10px;color:#888}
.post .meta b{color:var(--green)}
.legal{height:43px;background:var(--footer-bottom);color:#888;font-size:11px}
.legal .wrap{display:flex;justify-content:space-between;align-items:center;height:43px}
.socials{display:flex;gap:6px}
.socials span{width:26px;height:26px;border-radius:50%;border:1px solid #888}
</style>
</head>
<body>

<header class="site-header">
  <div class="wrap">
    <a class="brand" href="#"><span class="brand-mark"></span>Meridian Advisers</a>
    <nav class="main-nav">
      <a href="#">Investments</a>
      <a href="#">Get Financing</a>
      <a href="#">How It Works</a>
      <a href="#">Investment Adviser</a>
      <a href="#">Contact</a>
      <a class="btn btn-login" href="#">Login</a>
      <a class="btn btn-green" href="#">Get Started</a>
    </nav>
  </div>
</header>

<section class="hero">
  <div class="hero-photo" role="img" aria-label="Smiling couple looking out over a city skyline"></div>
  <div class="hero-copy">
    <h1>Real Estate Investing for<br>Apartment Properties</h1>
    <p>Our firm specializes in the sale of apartment properties in Southern California.<br>Get Sign up to access our investment opportunities.</p>
    <a class="btn btn-green" href="#">Join Now For FREE</a>
  </div>
  <div class="hero-dots"><span></span><span></span><span></span><span></span></div>
  <div class="stats">
    <div class="stat"><strong>125, 000 Investors</strong><small>Have joined Meridian.</small></div>
    <div class="stat"><strong>Over $850 Million</strong><small>Invested on our platform.</small></div>
    <div class="stat"><strong>$75 Million</strong><small>Paid out to Meridian investors.</small></div>
    <div class="stat"><strong>$0 Principal Lost</strong><small>By Meridian investors.</small></div>
  </div>
</section>

<section class="testimonial">
  <div class="wrap">
    <svg class="arrow" viewBox="0 0 20 20"><path d="M13 3 6 10l7 7" fill="none" stroke="#aaa" stroke-width="2"/></svg>
    <div class="avatar" role="img" aria-label="Client portrait"></div>
    <blockquote class="quote">" Class aptent taciti sociosqu ad litora torquent per conubia nostra, per inceptos himenaeos. Mauris in erat justo. Nullam ac urna eu felis dapibus condimentum sit amet a augue. "<cite>- Daniel Roe</cite></blockquote>
    <svg class="arrow" viewBox="0 0 20 20"><path d="m7 3 7 7-7 7" fill="none" stroke="#aaa" stroke-width="2"/></svg>
  </div>
</section>

<section class="intro">
  <div class="intro-copy">
    <h2>A completely new investing to<br>in Real Estate Properties</h2>
    <p>Class aptent taciti sociosqu ad litora torquent per conubia nostra, per inceptos himenaeos. Mauris in erat justo. Nullam ac urna eu felis dapibus condimentum sit amet a augue. Sed non neque elit. Sed ut imperdiet nisi. Proin condimentum fermentum nunc. Etiam pharetra, erat sed fermentum feugiat, velit mauris egestas quam, ut aliquam massa nisl quis neque. Suspendisse in orci enim.</p>
    <ul class="checks">
      <li><svg width="18" height="18" viewBox="0 0 18 18"><circle cx="9" cy="9" r="8" fill="none" stroke="#8cc63f"/><path d="m5 9 3 3 5-6" fill="none" stroke="#8cc63f" stroke-width="1.6"/></svg><span><b>Access</b> private real estate assets directly</span></li>
      <li><svg width="18" height="18" viewBox="0 0 18 18"><circle cx="9" cy="9" r="8" fill="none" stroke="#8cc63f"/><path d="m5 9 3 3 5-6" fill="none" stroke="#8cc63f" stroke-width="1.6"/></svg><span><b>Save</b> up to <span class="hl">40% on costs</span> through technology</span></li>
      <li><svg width="18" height="18" viewBox="0 0 18 18"><circle cx="9" cy="9" r="8" fill="none" stroke="#8cc63f"/><path d="m5 9 3 3 5-6" fill="none" stroke="#8cc63f" stroke-width="1.6"/></svg><span><b>Earn</b> better expected returns overall</span></li>
    </ul>
  </div>
  <div class="intro-device" role="img" aria-label="Laptop and phone showing investment dashboard charts"></div>
</section>

<section class="how">
  <div class="how-photo" role="img" aria-label="Man with glasses working at a laptop in a bright office"></div>
  <div class="how-copy">
    <h2>How It Works</h2>
    <div class="step"><h3>1. Invest</h3><p>Etiam pharetra, erat sed fermentum feugiat, velit mauris egestas quam, ut aliquam massa nisl quis neque.</p></div>
    <div class="step"><h3>2. Relax</h3><p>Etiam pharetra, erat sed fermentum feugiat, velit mauris egestas quam, ut aliquam massa nisl quis neque.</p></div>
    <div class="step"><h3>3. Get Paid</h3><p>Etiam pharetra, erat sed fermentum feugiat, velit mauris egestas quam, ut aliquam massa nisl quis neque.</p></div>
    <a class="btn btn-green" href="#">Get Started For FREE</a>
  </div>
</section>

<section class="split">
  <div class="panel panel-green" role="img" aria-label="Business team silhouettes in a city office, green tint">
    <h2>Not just changing,<br>How you invest, but What you invest in.</h2>
    <p>Class aptent taciti sociosqu ad litora torquent per conubia nostra, per inceptos himenaeos. Mauris in erat justo. Nullam ac urna eu felis dapibus condimentum sit amet a augue. Sed non neque elit. Sed ut imperdiet nisi. Proin condimentum fermentum nunc. Etiam pharetra, erat sed fermentum feugiat, velit mauris egestas quam, ut aliquam massa nisl quis neque. Suspendisse in orci enim.</p>
    <a class="btn btn-outline" href="#">Explore More</a>
  </div>
  <div class="panel panel-teal" role="img" aria-label="Businessman in an office, teal tint">
    <h2>Earn you higher expected returns<br>from&nbsp; Real Estate Properties</h2>
    <p>Class aptent taciti sociosqu ad litora torquent per conubia nostra, per inceptos himenaeos. Mauris in erat justo. Nullam ac urna eu felis dapibus condimentum sit amet a augue. Sed non neque elit. Sed ut imperdiet nisi. Proin condimentum fermentum nunc. Etiam pharetra, erat sed fermentum feugiat, velit mauris egestas quam, ut aliquam massa nisl quis neque. Suspendisse in orci enim.</p>
    <a class="btn btn-outline" href="#">Explore More</a>
  </div>
</section>

<section class="investments">
  <div class="wrap">
    <div class="investments-head"><h2>Recent Investments</h2><div class="slider-ctrl"><span></span><span></span></div></div>
    <div class="cards">
      <article class="card">
        <div class="card-photo" role="img" aria-label="Modern blue and white apartment building" style="background:linear-gradient(180deg,#3b7fd0,#1d3f8a)"></div>
        <h3>$2,030,200 Invested</h3>
        <p>Property Type : <b>Multifamily</b></p><p>Investment Type : <b>Equity</b></p><p>Location : <b>Hollywood</b></p>
      </article>
      <article class="card">
        <div class="card-photo" role="img" aria-label="Brick apartment block with lawn" style="background:linear-gradient(180deg,#8fb6d8,#a8583f)"></div>
        <h3>$1,030,200 Invested</h3>
        <p>Property Type : <b>Multifamily</b></p><p>Investment Type : <b>Equity</b></p><p>Location : <b>Hollywood</b></p>
      </article>
      <article class="card">
        <div class="card-photo" role="img" aria-label="White high-rise tower with palm trees" style="background:linear-gradient(180deg,#3d8fd6,#d8dde2 70%,#4c7a3a)"></div>
        <h3>$7,030,200 Invested</h3>
        <p>Property Type : <b>Multifamily</b></p><p>Investment Type : <b>Equity</b></p><p>Location : <b>Hollywood</b></p>
      </article>
      <article class="card">
        <div class="card-photo" role="img" aria-label="Apartment building with orange balconies" style="background:linear-gradient(180deg,#cfe0ee,#d8a14a 60%,#e6e3dc)"></div>
        <h3>$40,830,200 Invested</h3>
        <p>Property Type : <b>Multifamily</b></p><p>Investment Type : <b>Equity</b></p><p>Location : <b>Hollywood</b></p>
      </article>
    </div>
  </div>
</section>

<section class="cta" role="img" aria-label="Business meeting silhouettes against a bright window">
  <h2>Become a Real Estate Investor Today</h2>
  <p>Class aptent taciti sociosqu ad litora torquent per conubia nostra, per inceptos himenaeos. Mauris in erat justo. Nullam ac urna eu felis dapibus condimentum sit amet a augue. Sed non neque elit.</p>
  <a class="btn btn-green" href="#">Join Now For FREE</a>
</section>

<footer class="site-footer">
  <div class="wrap footer-cols">
    <div class="footer-col col-join">
      <h4>Join Newsletter</h4>
      <p>Enter Your email and receive latest<br>offer and news!</p>
      <span class="email-field">Email Address</span>
      <a class="subscribe" href="#">Subscribe</a>
    </div>
    <div class="footer-col col-sub">
      <h4>Subscribe Newsletter</h4>
      <p>Meridian Advisers<br>2210 Harbor Crest Ave,<br>Southern California 90210</p>
      <p style="margin-top:16px">T : +1 (555) 014 2870<br>E : hello@meridianadvisers.com<br>W : meridianadviser.com</p>
    </div>
    <div class="footer-col col-links">
      <h4>Quick Links</h4>
      <ul><li>Home</li><li>About Us</li><li>Services</li><li>Testimonials</li><li>Blog</li><li>Contact Us</li></ul>
    </div>
    <div class="footer-col col-blog">
      <h4>Recent Blog Posts</h4>
      <div class="post"><p class="meta">By <b>Daniel Roe</b> | 28 May 2017 | 0 Comments</p><p>Lorem Ipsum is simply dummy text of the printing typesetting industry.</p></div>
      <div class="post"><p class="meta">By <b>Daniel Roe</b> | 28 May 2017 | 0 Comments</p><p>Lorem Ipsum is simply dummy text of the printing typesetting industry.</p></div>
    </div>
  </div>
</footer>
<div class="legal">
  <div class="wrap">
    <span>Copyright ©2017 Meridian Advisers. Terms of Use | Privacy Policy | Sitemap</span>
    <div class="socials"><span></span><span></span><span></span><span></span><span></span></div>
  </div>
</div>

</body>
</html>
```